Massage Center New Ad

You will be creating a 5 X 7" Massage Ad.
All the text content remains the same as example provided
however looking for a "COMPLETELY DIFFERENT" Look.
Feel free to use photo images, clip art images, Black & white, etc. Remember it should different than example.
Emphasis on the PROMO of a 30 minute massage for Only $15. Logo Attached.
Reason: Still looking for the piece that stands out....Thanks
Massage

```html
<!DOCTYPE html>
<html lang="en">
<head>
<meta charset="utf-8">
<title>Coral Shore Massage Centers – $15 Massage</title>
<link href="https://fonts.googleapis.com/css2?family=Montserrat:wght@500;600;700;800&display=swap" rel="stylesheet">
<style>
  :root {
    --night: #13262a;
    --night-deep: #0c1a1d;
    --cream: #f4ede1;
    --sage: #9fc27a;
    --promo-red: #e23a2e;
    --promo-ring: #f4ede1;
    --photo-top: #6f8f5a;
    --photo-mid: #3f5a4a;
    --photo-low: #1f3035;
    --brand-dot: #f3a21c;
  }
  * { margin: 0; padding: 0; box-sizing: border-box; }
  html, body { width: 798px; height: 1200px; overflow: hidden; background: var(--night); }
  .ad {
    position: relative;
    width: 798px;
    height: 1200px;
    background: var(--night);
    font-family: "Montserrat", sans-serif;
    color: var(--cream);
    overflow: hidden;
  }
  .brand {
    position: absolute;
    top: 0; left: 0;
    width: 798px; height: 110px;
    display: flex;
    align-items: center;
    justify-content: center;
    gap: 16px;
  }
  .brand__dot {
    width: 30px; height: 30px;
    border-radius: 50%;
    background: var(--brand-dot);
  }
  .brand__name {
    font-weight: 700;
    font-size: 28px;
    letter-spacing: 1px;
    color: var(--cream);
  }
  .photo {
    position: absolute;
    top: 110px; left: 0;
    width: 798px; height: 410px;
    background: linear-gradient(180deg, var(--photo-top) 0%, var(--photo-mid) 55%, var(--photo-low) 100%);
  }
  .promo {
    position: absolute;
    top: 350px; left: 244px;
    width: 310px; height: 310px;
    border-radius: 50%;
    background: var(--promo-red);
    border: 8px solid var(--promo-ring);
    display: flex;
    flex-direction: column;
    align-items: center;
    justify-content: center;
    color: var(--cream);
    text-align: center;
  }
  .promo__only {
    font-weight: 600;
    font-size: 34px;
    letter-spacing: 4px;
    text-transform: uppercase;
    line-height: 1;
  }
  .promo__price {
    font-weight: 800;
    font-size: 120px;
    line-height: 1;
    margin: 6px 0 4px;
  }
  .promo__time {
    font-weight: 700;
    font-size: 38px;
    line-height: 1;
  }
  .headline {
    position: absolute;
    top: 690px; left: 0;
    width: 798px;
    text-align: center;
    font-weight: 800;
    font-size: 92px;
    letter-spacing: 14px;
    line-height: 1;
    padding-left: 14px;
    color: var(--cream);
  }
  .tagline {
    position: absolute;
    top: 800px; left: 0;
    width: 798px;
    text-align: center;
    font-weight: 600;
    font-size: 19px;
    letter-spacing: 3px;
    color: var(--sage);
  }
  .rule {
    position: absolute;
    top: 852px; left: 299px;
    width: 200px; height: 2px;
    background: var(--sage);
  }
  .services {
    position: absolute;
    top: 888px; left: 39px;
    width: 720px;
    list-style: none;
    display: grid;
    grid-template-columns: 1fr 1fr;
    column-gap: 20px;
    row-gap: 18px;
  }
  .services__item {
    display: flex;
    align-items: center;
    justify-content: center;
    gap: 10px;
    font-weight: 600;
    font-size: 22px;
    letter-spacing: 1px;
    line-height: 1.2;
    color: var(--cream);
  }
  .services__item::before {
    content: "";
    width: 8px; height: 8px;
    border-radius: 50%;
    background: var(--sage);
    flex: none;
  }
  .services__item--wide { grid-column: 1 / span 2; }
  .footer-band {
    position: absolute;
    bottom: 0; left: 0;
    width: 798px; height: 46px;
    background: var(--night-deep);
    border-top: 2px solid var(--sage);
  }
</style>
</head>
<body>
<main class="ad">
  <header class="brand">
    <span class="brand__dot"></span>
    <span class="brand__name">Coral Shore Massage Centers</span>
  </header>

  <div class="photo" role="img" aria-label="Warm spa stones stacked on a towel beside green bamboo leaves"></div>

  <div class="promo">
    <span class="promo__only">Only</span>
    <span class="promo__price">$15</span>
    <span class="promo__time">/30 min.</span>
  </div>

  <h1 class="headline">MASSAGE</h1>
  <p class="tagline">LICENSED PROFESSIONAL STRESS RELIEF</p>
  <div class="rule"></div>

  <ul class="services">
    <li class="services__item">SWEDISH</li>
    <li class="services__item">DEEP TISSUE</li>
    <li class="services__item">REFLEXOLOGY</li>
    <li class="services__item">INJURY MASSAGE</li>
    <li class="services__item">SPORTS MASSAGE</li>
    <li class="services__item">RELAXATION MASSAGE</li>
    <li class="services__item services__item--wide">TRIGGER POINT THERAPY</li>
  </ul>

  <div class="footer-band"></div>
</main>
</body>
</html>
```